International Consulting Firm
Stationery incl. business cards, letterhead, envelope, PPT template, and brochure
Professional
DMN QRT
CHIEF EXECUTIVE OFFICER
LEVEL 4,
7 MOOR LANE
FERN HOUSE
GOTHAM CITY
DMN@DORSETTPRYCE.EXAMPLE
WWW.DORSETTPRYCE.EXAMPLE
The fonts used in the logo are (a) Eras Bold ITC & (b)BankGothic
Logo only
This fantastic logo was designed recently by quarbin and we now need stationery to support it.

```html
<!DOCTYPE html>
<html lang="en">
<head>
<meta charset="utf-8">
<title>Dorsett Pryce Group — Stationery Set</title>
<link href="https://fonts.googleapis.com/css2?family=Michroma&family=Open+Sans:wght@400;600;700&display=swap" rel="stylesheet">
<style>
  :root{
    --copper-light:#c9935f;
    --copper-mid:#9a6235;
    --copper-dark:#4e2b14;
    --ink:#151515;
    --ink-soft:#2b2b2b;
    --grey:#8c8c8c;
    --grey-light:#d9d9d9;
    --paper:#ffffff;
    --accent:#2f8fd1;
    --text-light:#cfcfcf;
  }
  *{box-sizing:border-box;margin:0;padding:0}
  html,body{width:1200px;height:559px;overflow:hidden}
  body{
    position:relative;
    font-family:"Open Sans",Arial,sans-serif;
    background:radial-gradient(ellipse at 55% 45%,var(--copper-light) 0%,var(--copper-mid) 55%,var(--copper-dark) 100%);
    color:var(--ink);
  }
  .piece{position:absolute;overflow:hidden;box-shadow:2px 3px 8px rgba(0,0,0,.45)}
  .photo{position:absolute}
  .brand{display:flex;align-items:center;gap:4px;font-family:"Michroma",sans-serif;font-size:7px;color:var(--paper);letter-spacing:.3px;white-space:nowrap}
  .brand .dot{width:12px;height:12px;border-radius:50%;background:var(--paper);flex:none}
  .brand.dark{color:var(--ink)}
  .brand.dark .dot{background:var(--ink)}
  .swoosh{position:absolute;left:0;width:100%}
  .tiny{font-size:3.6px;line-height:5px;color:var(--text-light)}
  .tiny.dark{color:#555}
  .heading{font-size:5px;font-weight:700;color:var(--paper);margin-bottom:3px;letter-spacing:.4px}

  /* brochure */
  .brochure{display:flex}
  .panel{position:relative;flex:1;background:var(--ink);padding:8px 7px;border-right:1px solid #333}
  .brochure-outside{left:12px;top:8px;width:343px;height:207px}
  .brochure-inside{left:12px;top:228px;width:343px;height:318px}
  .bullets{list-style:none}
  .bullets li{font-size:3.8px;line-height:6px;color:var(--text-light)}
  .bullets li::before{content:"› ";color:var(--paper)}
  .tagline{position:absolute;left:8px;right:8px;top:70px;font-size:7px;font-weight:700;color:var(--accent);line-height:9px;text-align:center}
  .address{position:absolute;left:0;right:0;top:118px;text-align:center;font-size:4.2px;line-height:6px;color:var(--text-light);letter-spacing:.2px}

  /* letterhead, envelope */
  .letterhead{left:555px;top:15px;width:205px;height:262px;background:var(--paper)}
  .envelope{left:365px;top:170px;width:235px;height:130px;background:var(--paper)}
  .footer-line{position:absolute;left:10px;right:10px;font-size:3.6px;color:#666;letter-spacing:.2px}

  /* cards */
  .card{width:62px;height:38px;left:772px}
  .card-front{top:148px;background:var(--ink)}
  .card-back{top:198px;background:var(--paper)}

  /* form */
  .form{left:842px;top:15px;width:348px;height:262px;background:var(--paper);padding:10px 14px}
  .form-title{background:var(--ink);color:var(--paper);font-size:8px;font-weight:700;padding:3px 6px;letter-spacing:1px;width:100%}
  .form-table{width:100%;border-collapse:collapse;margin-top:2px}
  .form-table td{border:1px solid #999;height:11px;font-size:4.5px;padding:0 3px;color:#333}
  .form-table td.label{background:#eee;width:40px;font-weight:600}
  .checks{display:flex;gap:12px;margin-top:6px;font-size:4.5px;color:#333}
  .checks span::before{content:"";display:inline-block;width:5px;height:5px;border:1px solid #555;margin-right:2px;vertical-align:-1px}
  .form-lines{margin-top:8px;border-top:1px solid #bbb}
  .form-foot{position:absolute;left:14px;right:14px;bottom:8px;display:flex;justify-content:space-between;align-items:center}

  /* slides */
  .slide{top:330px;height:215px}
  .slide-title{left:365px;width:235px;background:var(--ink)}
  .slide-content{left:630px;width:290px;background:var(--paper)}
  .slide-thanks{left:935px;width:255px;background:var(--paper)}
  .slide-head{font-family:"Michroma",sans-serif;color:var(--paper);position:absolute;text-align:center;width:100%}
  .chart{position:absolute;border-left:1px solid #888;border-bottom:1px solid #888;display:flex;align-items:flex-end;gap:5px;padding:0 5px}
  .chart span{width:9px;background:linear-gradient(#bbb,#666)}
  .content-block{position:absolute;left:14px;width:140px}
  .content-block h4{font-size:6px;color:var(--ink);margin-bottom:2px}
</style>
</head>
<body>

<!-- Brochure outside -->
<section class="piece brochure brochure-outside" aria-label="Brochure outside">
  <div class="panel">
    <p class="heading">ABOUT US</p>
    <p class="tiny">We guide global firms through growth, change and risk with clear, tested advice. Our team works across markets to give leaders the insight they need to act with confidence and build lasting value.</p>
    <div class="photo" role="img" aria-label="Portrait photo of a consultant at a desk" style="left:6px;bottom:10px;width:52px;height:48px;background:linear-gradient(135deg,#6d7a86,#c7b8a3)"></div>
  </div>
  <div class="panel">
    <div class="brand" style="position:absolute;top:46px;left:50%;transform:translateX(-50%)"><span class="dot"></span>DORSETTPRYCE</div>
    <p class="address">DMN QRT<br>LEVEL 4,<br>7 MOOR LANE<br>FERN HOUSE<br>GOTHAM CITY<br>DMN@DORSETTPRYCE.EXAMPLE<br>WWW.DORSETTPRYCE.EXAMPLE</p>
  </div>
  <div class="panel" style="padding:0;background:#0e0e12">
    <div class="photo" role="img" aria-label="Photo of a tall office tower against the sky" style="left:0;top:0;width:100%;height:60px;background:linear-gradient(#8fa9c4,#3f4d5c)"></div>
    <p class="tagline">Empowered business solutions transforming industry</p>
    <div class="photo" role="img" aria-label="Photo of a hand touching glowing blue hexagons" style="left:0;bottom:0;width:100%;height:92px;background:linear-gradient(#1c3a63,#4f8fc8)"></div>
  </div>
</section>

<!-- Brochure inside -->
<section class="piece brochure brochure-inside" aria-label="Brochure inside">
  <div class="panel">
    <p class="heading">OUR APPROACH</p>
    <p class="tiny">Every project begins with listening. We study each market, map the risks and shape a plan that fits the people who deliver it.</p>
    <div class="photo" role="img" aria-label="Photo of a businesswoman in an office" style="left:0;bottom:0;width:100%;height:150px;background:linear-gradient(160deg,#b7b2ab,#3a3430)"></div>
  </div>
  <div class="panel">
    <div class="photo" role="img" aria-label="Photo of colleagues meeting around a table" style="left:0;top:0;width:100%;height:70px;background:linear-gradient(135deg,#d8d4cc,#7d8894)"></div>
    <p class="tiny" style="margin-top:68px">Strategy, finance and operations advice for firms expanding across borders, backed by partners on four continents.</p>
    <div class="photo" role="img" aria-label="Photo of a team of consultants smiling" style="left:0;bottom:0;width:100%;height:120px;background:linear-gradient(160deg,#c9c2b8,#4c4640)"></div>
  </div>
  <div class="panel">
    <p class="heading">SERVICES</p>
    <ul class="bullets">
      <li>Corporate strategy</li><li>Market entry</li><li>Risk review</li><li>Mergers support</li><li>Process design</li><li>Change management</li><li>Finance advisory</li>
    </ul>
    <div class="photo" role="img" aria-label="Photo of a businessman using a laptop" style="left:0;bottom:0;width:100%;height:130px;background:linear-gradient(160deg,#a9b1b8,#2f3438)"></div>
  </div>
</section>

<!-- Letterhead -->
<section class="piece letterhead" aria-label="Letterhead">
  <svg class="swoosh" style="top:0" width="205" height="60" viewBox="0 0 205 60" aria-hidden="true">
    <path d="M0 0H205V14C150 10 80 30 0 50Z" fill="var(--ink)"/>
    <path d="M0 55C80 34 150 16 205 20" stroke="var(--grey)" stroke-width="1.5" fill="none"/>
  </svg>
  <div class="brand" style="position:absolute;left:10px;top:10px"><span class="dot"></span>DORSETTPRYCE</div>
  <p class="footer-line" style="bottom:8px;text-align:center">Level 4, 7 Moor Lane, Fern House, Gotham City · www.dorsettpryce.example</p>
</section>

<!-- Envelope -->
<section class="piece envelope" aria-label="Envelope">
  <div class="brand dark" style="position:absolute;left:10px;top:10px"><span class="dot"></span>DORSETTPRYCE</div>
  <svg class="swoosh" style="bottom:0" width="235" height="50" viewBox="0 0 235 50" aria-hidden="true">
    <path d="M0 50V30C80 8 160 4 235 18V50Z" fill="var(--ink)"/>
    <path d="M0 24C80 2 160 0 235 12" stroke="var(--grey)" stroke-width="1.5" fill="none"/>
  </svg>
  <p class="footer-line" style="bottom:8px;color:var(--text-light)">Level 4, 7 Moor Lane, Fern House, Gotham City</p>
</section>

<!-- Business cards -->
<section class="piece card card-front" aria-label="Business card front">
  <div class="brand" style="position:absolute;left:6px;top:13px;font-size:5px"><span class="dot" style="width:8px;height:8px"></span>DORSETTPRYCE</div>
</section>
<section class="piece card card-back" aria-label="Business card back">
  <svg class="swoosh" style="top:0" width="62" height="14" viewBox="0 0 62 14" aria-hidden="true"><path d="M0 0H62V4C40 3 20 8 0 12Z" fill="var(--ink)"/></svg>
  <p class="tiny dark" style="position:absolute;left:4px;top:15px;font-size:3px;line-height:4px">DMN QRT<br>CHIEF EXECUTIVE OFFICER<br>DMN@DORSETTPRYCE.EXAMPLE</p>
</section>

<!-- Fax form -->
<section class="piece form" aria-label="Fax cover form">
  <p class="form-title">TITLE</p>
  <table class="form-table">
    <tr><td class="label">To</td><td></td><td class="label">From</td><td></td></tr>
    <tr><td class="label">Fax</td><td></td><td class="label">Pages</td><td></td></tr>
    <tr><td class="label">Phone</td><td></td><td class="label">Date</td><td></td></tr>
    <tr><td class="label">Re</td><td></td><td class="label">CC</td><td></td></tr>
  </table>
  <div class="checks"><span>Urgent</span><span>For Review</span><span>Please Comment</span><span>Please Reply</span><span>Please Recycle</span></div>
  <p style="font-size:4.5px;margin-top:5px;color:#333">Comments:</p>
  <div class="form-lines"></div>
  <div class="form-foot">
    <div class="brand dark"><span class="dot"></span>DORSETTPRYCE</div>
    <p style="font-size:3.6px;color:#666">Level 4, 7 Moor Lane, Fern House, Gotham City · +1 555 0142</p>
  </div>
</section>

<!-- Title slide -->
<section class="piece slide slide-title" aria-label="Presentation title slide">
  <div class="brand" style="position:absolute;left:10px;top:10px"><span class="dot"></span>DORSETTPRYCE</div>
  <div class="photo" role="img" aria-label="Faint photo of machine gears" style="left:40px;top:70px;width:150px;height:120px;border-radius:50%;background:radial-gradient(circle,#555 0%,#222 70%)"></div>
  <p class="slide-head" style="top:42px;font-size:14px">TITLE</p>
  <p class="slide-head" style="top:62px;font-size:9px">SUB TITLE</p>
  <svg class="swoosh" style="bottom:0" width="235" height="40" viewBox="0 0 235 40" aria-hidden="true">
    <path d="M0 16C80 0 160 0 235 14" stroke="var(--grey)" stroke-width="1.5" fill="none"/>
  </svg>
  <p class="footer-line" style="bottom:6px;color:var(--text-light)">www.dorsettpryce.example</p>
</section>

<!-- Content slide -->
<section class="piece slide slide-content" aria-label="Presentation content slide">
  <svg class="swoosh" style="top:0" width="290" height="50" viewBox="0 0 290 50" aria-hidden="true">
    <path d="M0 0H290V36C200 22 100 28 0 44Z" fill="var(--ink)"/>
  </svg>
  <p class="slide-head" style="top:14px;font-size:9px">SUB TITLE</p>
  <div class="content-block" style="top:62px">
    <h4>TITLE</h4>
    <p class="tiny dark">Revenue across our three core regions rose steadily this year, led by strong demand in advisory and market entry work.</p>
  </div>
  <div class="content-block" style="top:128px">
    <h4>TITLE</h4>
    <p class="tiny dark">Client retention stayed high while new sectors added fresh growth and widened our reach into emerging markets.</p>
  </div>
  <div class="chart" style="left:175px;top:60px;width:95px;height:50px"><span style="height:35%"></span><span style="height:55%"></span><span style="height:70%"></span><span style="height:90%"></span></div>
  <div class="chart" style="left:175px;top:130px;width:95px;height:50px"><span style="height:45%"></span><span style="height:60%"></span><span style="height:75%"></span><span style="height:85%"></span></div>
  <p class="footer-line" style="bottom:6px">www.dorsettpryce.example</p>
</section>

<!-- Closing slide -->
<section class="piece slide slide-thanks" aria-label="Presentation closing slide">
  <p class="slide-head" style="top:90px;font-size:18px;color:var(--ink)">THAN YOU</p>
  <div class="brand dark" style="position:absolute;left:14px;bottom:14px"><span class="dot"></span>DORSETTPRYCE</div>
</section>

</body>
</html>
```